New look and feel for Corvel Sound

We need landing page designs for our company that manufactures high end bass guitars and related electronic products. We will be using premier musicians to promote the product on the site. We have recently designed a new logo, which is in the upload files. A link to our Facebook page is at www.corvelsound.example

Target Market(s)

Professional Musicians and serious Amateurs

Industry/Entity Type

Electronic

Number of Pages Required

5+ page

Font styles to use
Serif

Requirements
Must have
• Utilize images of product and endorsing musicians to promote drive interest
Should not have
• Anything that is outer space or "alien" looking

```html
<!DOCTYPE html>
<html lang="en">
<head>
<meta charset="utf-8">
<title>Corvel Sound</title>
<link rel="stylesheet" href="https://fonts.googleapis.com/css2?family=Roboto:wght@300;400;500;700&display=swap">
<style>
:root{
  --page:#121314;
  --teal:#3cc6d3;
  --band:#1c5fc0;
  --band-deep:#17469a;
  --text:#ffffff;
  --muted:#b9c6d8;
  --footer:#0a0a0a;
  --footer-line:#222;
}
*{margin:0;padding:0;box-sizing:border-box}
html,body{width:719px;height:1200px;overflow:hidden;background:var(--page)}
body{font-family:"Roboto",Arial,sans-serif;color:var(--text);position:relative}
a{color:inherit;text-decoration:none}

.site-header{position:absolute;top:0;left:0;width:719px;height:76px;background:rgba(8,8,9,.85);display:flex;align-items:center;justify-content:space-between;padding:0 22px 0 36px;z-index:2;white-space:nowrap}
.brand{display:flex;align-items:center;gap:8px;font-weight:700;font-size:22px;color:var(--text);white-space:nowrap}
.brand-dot{width:18px;height:18px;border-radius:50%;background:var(--teal)}
.main-nav{display:flex;gap:16px;font-size:11px;font-weight:500;white-space:nowrap}
.main-nav a{white-space:nowrap}
.main-nav a.active{color:var(--teal)}

.hero-photo{position:absolute;top:0;left:0;width:719px;height:380px;
  background:
    radial-gradient(ellipse 90px 120px at 370px 200px,rgba(214,170,130,.55) 0%,rgba(120,90,80,.25) 55%,transparent 100%),
    linear-gradient(160deg,transparent 40%,rgba(60,110,220,.55) 52%,transparent 60%),
    radial-gradient(ellipse 230px 180px at 360px 230px,#2a2f48 0%,#15161f 70%,transparent 100%),
    linear-gradient(180deg,#0b0b0e 0%,#1a1b22 55%,#0c0c0f 100%)}

.artist-band{position:absolute;top:380px;left:0;width:719px;height:244px;background:linear-gradient(90deg,var(--band) 0%,var(--band-deep) 100%)}
.artist-info{position:absolute;left:56px;top:22px;width:260px}
.artist-name{font-size:24px;font-weight:400;color:var(--teal);white-space:nowrap}
.artist-quote{margin-top:12px;font-size:11px;line-height:1.45;color:var(--text)}
.artist-bio{margin-top:12px;font-size:9.5px;line-height:1.55;color:var(--muted)}
.btn-artists{display:inline-block;margin-top:14px;background:var(--teal);color:#0d2a40;font-size:12px;font-weight:500;padding:6px 12px}
.social-small{display:flex;gap:12px;margin-top:12px}
.social-small span{width:8px;height:8px;border-radius:50%;background:#fff}
.artist-photo{position:absolute;left:372px;top:0;width:347px;height:244px;
  background:
    radial-gradient(ellipse 60px 80px at 215px 70px,rgba(220,200,230,.55) 0%,transparent 100%),
    radial-gradient(ellipse 120px 140px at 200px 150px,#3b3fd8 0%,transparent 100%),
    linear-gradient(120deg,#1d1f6a 0%,#2f33b8 45%,#151750 100%)}

.featured{position:absolute;top:624px;left:0;width:719px;height:494px;text-align:center}
.featured-title{margin-top:40px;font-size:34px;font-weight:400;color:var(--teal)}
.video-frame{position:absolute;left:140px;top:118px;width:438px;height:240px;
  background:
    radial-gradient(ellipse 90px 110px at 210px 150px,rgba(200,170,150,.5) 0%,transparent 100%),
    radial-gradient(ellipse 160px 80px at 120px 40px,rgba(210,60,70,.55) 0%,transparent 100%),
    radial-gradient(ellipse at 50% 40%,#6a3a3a 0%,#3a2226 50%,#141012 100%)}
.video-caption{position:absolute;top:376px;width:100%;font-size:12px;color:#ddd}
.btn-videos{position:absolute;left:282px;top:402px;width:155px;height:42px;border:1px solid #bbb;font-size:16px;line-height:40px;color:var(--text)}

.site-footer{position:absolute;top:1118px;left:0;width:719px;height:82px;background:var(--footer);border-top:1px solid var(--footer-line)}
.footer-nav{position:absolute;left:46px;top:30px;display:flex;gap:22px;font-size:10px;color:#ccc;white-space:nowrap}
.footer-nav a.active{color:var(--teal)}
.copyright{position:absolute;left:46px;top:48px;font-size:8px;color:var(--teal);white-space:nowrap}
.footer-social{position:absolute;right:50px;top:20px;display:flex;gap:14px}
.footer-social span{width:30px;height:30px;border-radius:50%;background:#1c1c1c;border:1px solid #333}
</style>
</head>
<body>
<header class="site-header">
  <a class="brand" href="#"><span class="brand-dot"></span>Corvel Sound</a>
  <nav class="main-nav">
    <a class="active" href="#">HOME</a><a href="#">BASSES</a><a href="#">PRE AMPS</a><a href="#">ARTISTS</a><a href="#">WHERE TO BUY</a><a href="#">ABOUT</a><a href="#">CONTACT</a>
  </nav>
</header>

<div class="hero-photo" role="img" aria-label="Bassist on stage playing a blue bass guitar"></div>

<section class="artist-band">
  <div class="artist-info">
    <h2 class="artist-name">Dale Harwick</h2>
    <p class="artist-quote">Dale Harwick with Meridian "The best instrument I have ever played" Low End Monthly Oct, 2015</p>
    <p class="artist-bio">Lorem ipsum is simply dummy text of the printing and typesetting industry. Lorem Ipsum has been the industry's standard dummy text ever since the 1500.</p>
    <a class="btn-artists" href="#">ARTISTS</a>
    <div class="social-small"><span></span><span></span><span></span><span></span></div>
  </div>
  <div class="artist-photo" role="img" aria-label="Bassist performing live under blue stage lights"></div>
</section>

<section class="featured">
  <h2 class="featured-title">Featured Video</h2>
  <div class="video-frame" role="img" aria-label="Concert video of a bassist performing"></div>
  <p class="video-caption">Meridian 99 / The Muse at the Harbor Theater 2014</p>
  <a class="btn-videos" href="#">See All Videos</a>
</section>

<footer class="site-footer">
  <nav class="footer-nav">
    <a class="active" href="#">HOME</a><a href="#">BASSES</a><a href="#">PRE AMPS</a><a href="#">ARTISTS</a><a href="#">WHERE TO BUY</a><a href="#">ABOUT</a><a href="#">CONTACT</a>
  </nav>
  <p class="copyright">© Corvel Sound - 2015. All Rights Reserved</p>
  <div class="footer-social"><span></span><span></span><span></span></div>
</footer>
</body>
</html>
```